New Webpage for High Class Expert Witness Services Company

We are looking for a minimalist design for a webpage that just has our logo and an entry form offer to connect with one of our Liaisons.
The entry form should just ask for Name, Email, Contact Info and Description of Project.

Company Name is: The Marlow Crest Advisory Services

Number of Pages Required

1 page

```html
<!DOCTYPE html>
<html lang="en">
<head>
<meta charset="utf-8">
<title>The Marlow Crest Advisory Services — Request a Liaison</title>
<link href="https://fonts.googleapis.com/css2?family=Cormorant+Garamond:wght@400;500&family=Inter:wght@400;500;600&display=swap" rel="stylesheet">
<style>
  :root {
    --page-bg: #0d0d0e;
    --page-glow: #1c1c1e;
    --text-primary: #eceae6;
    --text-secondary: #a9a9ab;
    --text-muted: #8a8a8d;
    --label: #c9c9cb;
    --rule: #2a2a2c;
    --panel-border: #2e2e30;
    --field-bg: #202022;
    --field-border: #343437;
    --placeholder: #7d7d80;
    --button-bg: #c3c7ca;
    --button-text: #1a1a1c;
  }
  * { box-sizing: border-box; margin: 0; padding: 0; }
  html, body { width: 1200px; height: 1200px; overflow: hidden; }
  body {
    background: radial-gradient(ellipse 60% 45% at 30% 45%, var(--page-glow), var(--page-bg) 70%);
    color: var(--text-primary);
    font-family: "Inter", sans-serif;
  }
  .page {
    width: 1200px; height: 1200px;
    padding: 0 80px;
    display: flex; flex-direction: column;
  }
  .main {
    flex: 1;
    display: grid;
    grid-template-columns: 1fr 540px;
    gap: 60px;
    align-items: center;
  }
  .intro { text-align: center; }
  .brand {
    display: inline-flex; align-items: center; gap: 14px;
    font-family: "Cormorant Garamond", serif;
    font-weight: 500;
    font-size: 27px;
    letter-spacing: 0.06em;
    text-transform: uppercase;
    color: var(--text-primary);
    line-height: 1.15;
  }
  .brand-mark { width: 20px; height: 20px; border: 1.5px solid var(--text-primary); flex: none; }
  .brand-name { text-align: left; }
  .intro-rule {
    width: 90px; height: 1px; margin: 40px auto 36px;
    background: linear-gradient(90deg, transparent, #6a6a6d, transparent);
  }
  .intro-heading {
    font-family: "Cormorant Garamond", serif;
    font-weight: 400;
    font-size: 29px;
    line-height: 1.45;
    color: var(--text-primary);
  }
  .heading-line { display: block; white-space: nowrap; }
  .intro-copy {
    margin-top: 22px;
    font-size: 14.5px;
    line-height: 1.85;
    color: var(--text-secondary);
  }
  .request { display: flex; flex-direction: column; }
  .request-title {
    display: flex; align-items: center; gap: 16px;
    font-family: "Cormorant Garamond", serif;
    font-size: 13px; letter-spacing: 0.34em;
    color: var(--text-muted);
    text-transform: uppercase;
    margin-bottom: 28px;
  }
  .request-title::before, .request-title::after {
    content: ""; flex: 1; height: 1px;
    background: linear-gradient(90deg, transparent, var(--rule));
  }
  .request-title::after { background: linear-gradient(90deg, var(--rule), transparent); }
  .request-form {
    border: 1px solid var(--panel-border);
    border-radius: 3px;
    padding: 30px 28px 28px;
  }
  .field { margin-bottom: 26px; }
  .field-label {
    display: block;
    font-size: 11px; font-weight: 600;
    letter-spacing: 0.16em;
    color: var(--label);
    text-transform: uppercase;
    margin-bottom: 8px;
  }
  .field-input {
    width: 100%; height: 44px;
    background: var(--field-bg);
    border: 1px solid var(--field-border);
    border-radius: 3px;
    padding: 0 14px;
    font-family: "Inter", sans-serif;
    font-size: 15px;
    color: var(--text-primary);
  }
  textarea.field-input { height: 88px; padding: 12px 14px; resize: none; }
  .field-input::placeholder { color: var(--placeholder); }
  .submit {
    width: 100%; height: 50px; margin-top: 2px;
    background: var(--button-bg);
    color: var(--button-text);
    border: none; border-radius: 2px;
    font-family: "Cormorant Garamond", serif;
    font-size: 18px; letter-spacing: 0.03em;
  }
  .form-note {
    margin-top: 26px;
    text-align: center;
    font-size: 12.5px;
    color: var(--text-secondary);
  }
  .footer {
    border-top: 1px solid var(--rule);
    padding: 22px 0 40px;
    display: flex; justify-content: space-between; align-items: center;
  }
  .copyright {
    font-family: "Cormorant Garamond", serif;
    font-size: 14px; color: var(--text-muted);
  }
  .contact-email { font-size: 14px; color: var(--text-secondary); }
</style>
</head>
<body>
  <div class="page">
    <main class="main">
      <section class="intro">
        <div class="brand">
          <span class="brand-mark"></span>
          <span class="brand-name">Marlow Crest<br>Advisory Services</span>
        </div>
        <div class="intro-rule"></div>
        <h1 class="intro-heading">
          <span class="heading-line">Connect with a Liaison to discuss</span>
          <span class="heading-line">your case.</span>
        </h1>
        <p class="intro-copy">A discreet point of contact for sensitive matters. Share the essentials and a Liaison will respond personally, in confidence, without obligation.</p>
      </section>

      <section class="request">
        <h2 class="request-title">Request a Liaison</h2>
        <form class="request-form">
          <div class="field">
            <label class="field-label" for="name">Full Name</label>
            <input class="field-input" id="name" type="text" placeholder="Your name">
          </div>
          <div class="field">
            <label class="field-label" for="email">Email</label>
            <input class="field-input" id="email" type="email" placeholder="you@example.com">
          </div>
          <div class="field">
            <label class="field-label" for="contact">Contact Info</label>
            <input class="field-input" id="contact" type="text" placeholder="Phone, messaging app, or preferred channel">
          </div>
          <div class="field">
            <label class="field-label" for="project">Description of Project</label>
            <textarea class="field-input" id="project" placeholder="Briefly outline the matter you'd like to discuss."></textarea>
          </div>
          <button class="submit" type="button">Request a Liaison</button>
          <p class="form-note">Your information is treated with the utmost discretion.</p>
        </form>
      </section>
    </main>

    <footer class="footer">
      <span class="copyright">© 2026 The Marlow Crest Advisory Services</span>
      <span class="contact-email">liaison@marlowcrest.com</span>
    </footer>
  </div>
</body>
</html>
```